Business school needs a web design

Who We are:
KRVT is a small business school that offers programs in Project Management. The school is based in West Africa and welcomes students from the whole area. Our aim is to become one of the reference business schools in Africa.

Project Brief:
The site will include all informations relevant for different types of visitors that we have: actual and future students, companies, mass media, future employees, ect. It will present information about subscription, list of programs, presentation of the school and its team,etc.

What We want:
This competition is for Design only no coding! We need design for two pages.
We did some wireframing for the home page and the list of programs page. We made them just to show how we imagine the website would look like. But we encourage creative designs, so you don't have to stick to the wireframe models.

Sites We like:
http://www.ravenmoorcollege.example/
http://www.belvantis.example/fr/etudes.html
http://www.qtl.example/mba/Pages/default.aspx

Color schemes
The logo of the school is red and black. So the color scheme of the website should match that. For the rest, it is opened to your imagination.
Updates

The payment for the project is now garanteed. Good luck to you all !

Target Market(s)

The target market is diversified because we have students of different ages, also company representatives or employees that might visit the website for recruitment purposes. But the majority of our audience should be aged between 20 - 30 years.

Industry/Entity Type

Small Business

Requirements
Must have
• The design must include two pages: a home page and another interior page : might be the list of programs or any other page relevant to the domain. The Home page must include a slide show at the beginning.
The background page must be white.
Nice to have
• The use of flat design for this project is preferred.
The use of Pelican scaffold as a base for the design is an asset.

```html
<!DOCTYPE html>
<html lang="fr">
<head>
<meta charset="utf-8">
<title>KRVT — École de gestion de projet</title>
<link href="https://fonts.googleapis.com/css2?family=Oxygen:wght@400;700&family=Roboto:wght@500;700&display=swap" rel="stylesheet">
<style>
:root{
  --red:#c4161c;
  --red-dark:#9c0f14;
  --ink:#333;
  --ink-soft:#555;
  --grey-line:#d5d5d5;
  --page:#f4f1ee;
  --card:#fff;
  --footer:#1c1c1c;
  --band:#3a3a3a;
}
*{margin:0;padding:0;box-sizing:border-box}
html,body{width:931px;height:1200px;overflow:hidden}
body{position:relative;background:var(--page);font-family:'Oxygen',sans-serif;color:var(--ink);font-size:10px}
a{color:inherit;text-decoration:none}
.abs{position:absolute}
h2,h3{font-family:'Roboto',sans-serif;font-weight:700;color:#333}

.site-header{left:0;top:0;width:931px;height:82px;background:linear-gradient(#fff,#ebebeb);border-bottom:1px solid #ddd}
.brand{left:108px;top:22px;display:flex;align-items:center;gap:6px;font-family:'Oxygen',sans-serif;font-weight:700;font-size:22px;color:var(--red)}
.brand .dot{width:16px;height:16px;border-radius:50%;background:#111}
.util-links{right:115px;top:6px;font-size:9.5px;color:#666}
.util-links span{margin:0 4px;color:#aaa}
.phone{right:105px;top:28px;font-size:11px;font-weight:700;color:var(--red);display:flex;align-items:center;gap:3px}
.main-nav{left:229px;top:44px;display:flex;height:32px}
.main-nav a{display:flex;align-items:center;padding:0 6px;font-size:10.5px;color:#444;background:#f0f0f0;border-right:1px solid #ddd}
.main-nav a.active{background:var(--red);color:#fff;border-radius:3px 3px 0 0;width:99px;justify-content:center}
.search{left:732px;top:49px;width:94px;height:21px;background:#fff;border:1px solid #ddd;font-size:10px;color:var(--red);padding:3px 5px}
.search svg{position:absolute;right:4px;top:3px}

.hero{left:0;top:82px;width:931px;height:259px;background:linear-gradient(90deg,#5a5a60,#b8b4b0 30%,#d8d2cc 50%,#a8a6a8 75%,#505258)}
.hero-arrow{width:31px;height:31px;border-radius:50%;background:rgba(255,255,255,.85);display:flex;align-items:center;justify-content:center;top:181px}

.card{left:94px;top:318px;width:743px;height:846px;background:var(--card);border-radius:6px;box-shadow:0 1px 4px rgba(0,0,0,.15)}

.mini-brand{left:140px;top:345px;font-weight:700;font-size:15px;color:var(--red);display:flex;align-items:center;gap:4px}
.mini-brand .dot{width:11px;height:11px;border-radius:50%;background:#111}
.band{left:88px;width:166px;height:28px;background:linear-gradient(#555,#2a2a2a);color:#fff;font-family:'Oxygen',sans-serif;font-size:16px;display:flex;align-items:center;padding-left:44px;clip-path:polygon(0 0,92% 0,100% 50%,92% 100%,0 100%)}
.audience{left:114px;top:414px;list-style:none}
.audience li{font-size:11.5px;height:25.6px;color:#333}
.bullet{color:var(--red);margin-right:4px}
.video{left:116px;top:648px;width:128px;height:68px;background:linear-gradient(135deg,#c9b79a,#d9c23a 55%,#6e6658);border:2px solid #222;border-bottom-width:10px}

.intro-title{left:270px;top:328px;font-size:16px}
.intro-text{left:270px;top:358px;width:365px;font-size:9.6px;line-height:15px;color:#555}
.more{color:var(--red);font-size:9.5px}
.sec-title{font-size:16px;border-bottom:1px solid #ddd;padding-bottom:3px}
.tile{width:101px;height:101px;border-radius:3px}
.tile-cap{width:120px;text-align:center;font-size:9.5px;font-weight:700;color:var(--red);line-height:10px}
.blog{width:100px}
.blog .thumb{width:96px;height:51px;border:2px solid #777;background:linear-gradient(135deg,#9aa2a8,#d8c040 55%,#7c7a74)}
.blog .date{font-size:9.5px;font-weight:700;color:var(--red);margin-top:5px}
.blog .t{font-size:9.5px;font-weight:700;margin-top:3px}
.blog p{font-size:9.6px;line-height:13px;color:#555;letter-spacing:.3px}

.side-title{left:657px;font-size:16px;width:140px;border-bottom:1px solid #ddd;padding-bottom:3px}
.links{left:657px;top:357px;list-style:none}
.links li{font-size:10px;height:19.6px;color:#444}
.news{left:658px;width:170px;display:flex;gap:4px}
.news .thumb{width:48px;height:48px;flex:none;background:linear-gradient(135deg,#9aa2a8,#d8c040 55%,#7c7a74)}
.news p{font-size:9.5px;line-height:15px;color:#555}

.rule{left:114px;width:710px;height:1px;background:#e2e2e2}
.event{width:325px;display:flex;gap:5px}
.datebox{width:24px;height:26px;border:1px solid #999;border-radius:2px;flex:none;text-align:center;font-size:8.5px;line-height:12px}
.datebox b{display:block;background:#777;color:#fff;font-weight:400}
.datebox i{font-style:normal;font-weight:700;color:var(--red)}
.event p{font-size:9.6px;line-height:14px;color:#444}

.partner-arrow{width:20px;height:20px;border-radius:50%;background:#e6e6e6;display:flex;align-items:center;justify-content:center;top:936px}
.partners{left:150px;top:930px;width:640px;display:flex;justify-content:space-around;align-items:center;height:32px}
.partners span{font-family:'Roboto',sans-serif;font-weight:700;font-size:24px;color:#2b4a8c}

.footer{left:94px;top:992px;width:743px;height:148px;background:var(--footer);border-radius:0 0 6px 6px;color:#fff}
.fcol{top:1000px}
.fcol h4{font-family:'Oxygen',sans-serif;font-size:13px;font-weight:700;padding-bottom:6px;border-bottom:1px dotted #888;width:100px;margin-bottom:8px}
.fcol li{list-style:none;font-size:9.5px;height:22.6px;color:#eee}
.social li{display:flex;align-items:center;gap:9px;height:26px}
.sq{width:18px;height:18px;border-radius:3px}
.fcol p{font-size:9.3px;line-height:12px;color:#eee}
.news-form{left:709px;top:1107px;width:116px;height:18px;background:#fff;border-radius:3px 9px 9px 3px;display:flex;justify-content:flex-end}
.news-form span{font-size:9.5px;font-weight:700;color:#555;border-left:1px solid #ccc;padding:3px 7px}
.copy{left:0;top:1146px;width:931px;text-align:center;font-size:9.5px;color:var(--red)}
</style>
</head>
<body>

<header class="abs site-header">
  <div class="abs brand"><span class="dot"></span>KRVT</div>
  <div class="abs util-links">Repertoire du personnel<span>|</span>Blogue<span>|</span>Solle de presse<span>|</span>Nous joindre<span>|</span>English</div>
  <div class="abs phone"><svg width="8" height="11" viewBox="0 0 8 11"><path d="M2 0h2l1 3-1.5 1c.5 1.5 1 2.5 2 3.2L7 6l1 3-1 2C3 10 0 5 2 0z" fill="#111"/></svg>(000) 41 552 18 30</div>
  <nav class="abs main-nav">
    <a class="active" href="#">A Propos de l'krvt</a>
    <a href="#">Programmes et Formations</a>
    <a href="#">Etudiants</a>
    <a href="#">Nouvelles et Evenements</a>
    <a href="#">Enterprises</a>
  </nav>
  <div class="abs search">Search<svg width="14" height="14" viewBox="0 0 14 14"><circle cx="6" cy="6" r="4.5" fill="none" stroke="#c4161c" stroke-width="1.4"/><path d="M9.5 9.5L13 13" stroke="#c4161c" stroke-width="1.4"/></svg></div>
</header>

<div class="abs hero" role="img" aria-label="Photo de groupe de professionnels souriants en tenue d'affaires"></div>
<div class="abs hero-arrow" style="left:115px"><svg width="12" height="14" viewBox="0 0 12 14"><path d="M9 1L3 7l6 6" fill="none" stroke="#c4161c" stroke-width="3"/></svg></div>
<div class="abs hero-arrow" style="left:799px"><svg width="12" height="14" viewBox="0 0 12 14"><path d="M3 1l6 6-6 6" fill="none" stroke="#c4161c" stroke-width="3"/></svg></div>

<main class="abs card"></main>

<div class="abs mini-brand"><span class="dot"></span>KRVT</div>
<div class="abs band" style="top:378px">Vous etes</div>
<ul class="abs audience">
  <li><span class="bullet">•</span>Future etudiant</li>
  <li><span class="bullet">•</span>Etudiant actuel</li>
  <li><span class="bullet">•</span>Entreprise</li>
  <li><span class="bullet">•</span>Employeur</li>
  <li><span class="bullet">•</span>Postulant</li>
  <li><span class="bullet">•</span>Medias</li>
  <li><span class="bullet">•</span>Partenaires</li>
</ul>
<div class="abs band" style="top:598px;padding-left:44px">KRVT.tv</div>
<div class="abs video" role="img" aria-label="Lecteur vidéo : étudiante écrivant en classe"></div>

<h2 class="abs intro-title">Devenez Les Gestionnaires De Demain</h2>
<div class="abs intro-text">Lorem ipsum dolor sit amet, consectetuer adipiscing elit, sed diam nonummy nibh euismod tincidunt ut laoreet dolore magna aliquam erat volutpat. Ut wisi enim ad.<br><a class="more" href="#">Lira la suite</a></div>

<h3 class="abs sec-title" style="left:270px;top:410px;width:250px">A-B-C de la demande d’admission</h3>
<div class="abs tile" style="left:270px;top:446px;background:linear-gradient(135deg,#c8a060,#c43a2a 50%,#2f6a3a)" role="img" aria-label="Pile de manuels scolaires colorés"></div>
<div class="abs tile" style="left:401px;top:446px;background:linear-gradient(135deg,#eee,#444 60%,#111)" role="img" aria-label="Femme en tailleur devant un écran"></div>
<div class="abs tile" style="left:530px;top:446px;background:linear-gradient(135deg,#f0e8dc,#b08868 55%,#333)" role="img" aria-label="Femme consultant une tablette"></div>
<div class="abs tile-cap" style="left:261px;top:553px">Choix d’un<br>programme d’études</div>
<div class="abs tile-cap" style="left:391px;top:553px">Revue des<br>préalables</div>
<div class="abs tile-cap" style="left:520px;top:553px">Création d’un<br>profil personnel</div>

<h3 class="abs sec-title" style="left:270px;top:584px;width:56px">Blouge</h3>
<div class="abs blog" style="left:270px;top:616px"><div class="thumb" role="img" aria-label="Étudiante en examen"></div><div class="date">Jan 11, 2014</div><div class="t">Title</div><p>Lorem ipsum dolor sit amet consectetue</p><a class="more" href="#">Lira la suite</a></div>
<div class="abs blog" style="left:401px;top:616px"><div class="thumb" role="img" aria-label="Étudiante en examen"></div><div class="date">Jan 11, 2014</div><div class="t">Title</div><p>Lorem ipsum dolor sit amet consectetue</p><a class="more" href="#">Lira la suite</a></div>
<div class="abs blog" style="left:530px;top:616px"><div class="thumb" role="img" aria-label="Étudiante en examen"></div><div class="date">Jan 11, 2014</div><div class="t">Title</div><p>Lorem ipsum dolor sit amet consectetue</p><a class="more" href="#">Lira la suite</a></div>

<h3 class="abs side-title" style="top:328px">Lorem ipsum dolor</h3>
<ul class="abs links">
  <li><span class="bullet">•</span>Demande d’admission</li>
  <li><span class="bullet">•</span>Activités de recrutement</li>
  <li><span class="bullet">•</span>Enseignement coopératif</li>
  <li><span class="bullet">•</span>Programmes de premier cycle</li>
  <li><span class="bullet">•</span>Programmes d’études supérieures</li>
</ul>
<h3 class="abs side-title" style="top:458px;width:140px">Nouvelles</h3>
<div class="abs news" style="top:493px"><div class="thumb" role="img" aria-label="Étudiante en examen"></div><p>Lorem ipsum dolor sit amet, consectetuer adipiscing elit<br><a class="more" href="#" style="font-weight:700">Lira la suite</a></p></div>
<div class="abs news" style="top:553px"><div class="thumb" role="img" aria-label="Étudiante en examen"></div><p>Lorem ipsum dolor sit amet, consectetuer adipiscing elit<br><a class="more" href="#" style="font-weight:700">Lira la suite</a></p></div>
<div class="abs news" style="top:614px"><div class="thumb" role="img" aria-label="Étudiante en examen"></div><p>Lorem ipsum dolor sit amet, consectetuer adipiscing elit<br><a class="more" href="#" style="font-weight:700">Lira la suite</a></p></div>
<div class="abs news" style="top:676px"><div class="thumb" role="img" aria-label="Étudiante en examen"></div><p>Lorem ipsum dolor sit amet, consectetuer adipiscing elit<br><a class="more" href="#" style="font-weight:700">Lira la suite</a></p></div>

<div class="abs rule" style="top:754px"></div>
<h3 class="abs" style="left:114px;top:764px;font-size:16px">Evenements</h3>
<div class="abs event" style="left:114px;top:794px"><div class="datebox"><b>JAN</b><i>12</i></div><p>Lorem ipsum dolor sit amet, consectetuer adipiscing elit, sed diam nonummy nibh euismod tincidunt ut laoreet dolore magna aliquam erat volutpat.<br><a class="more" href="#">&nbsp;Lira la suite</a></p></div>
<div class="abs event" style="left:502px;top:794px"><div class="datebox"><b>JAN</b><i>12</i></div><p>Lorem ipsum dolor sit amet, consectetuer adipiscing elit, sed diam nibh euismod tincidunt ut laoreet dolore magna aliquam erat.<br><a class="more" href="#">&nbsp;Lira la suite</a></p></div>
<div class="abs event" style="left:114px;top:848px"><div class="datebox"><b>JAN</b><i>12</i></div><p>Lorem ipsum dolor sit amet, consectetuer adipiscing elit, sed diam nonummy nibh euismod tincidunt ut laoreet dolore magna aliquam erat volutpat.<br><a class="more" href="#">&nbsp;Lira la suite</a></p></div>
<div class="abs event" style="left:502px;top:848px"><div class="datebox"><b>JAN</b><i>12</i></div><p>Lorem ipsum dolor sit amet, consectetuer adipiscing elit, sed diam nibh euismod tincidunt ut laoreet dolore magna aliquam erat.<br><a class="more" href="#">&nbsp;Lira la suite</a></p></div>

<div class="abs rule" style="top:906px"></div>
<div class="abs partner-arrow" style="left:118px"><svg width="8" height="10" viewBox="0 0 8 10"><path d="M6 1L2 5l4 4" fill="none" stroke="#555" stroke-width="1.8"/></svg></div>
<div class="abs partners"><span>Orvalis</span><span>Tessaline</span><span style="color:#555">Brindmark</span><span style="color:#2a5a3a">Quorvex</span></div>
<div class="abs partner-arrow" style="left:803px"><svg width="8" height="10" viewBox="0 0 8 10"><path d="M2 1l4 4-4 4" fill="none" stroke="#555" stroke-width="1.8"/></svg></div>

<footer class="abs footer"></footer>
<div class="abs fcol" style="left:118px"><h4>Suivez - nous &gt;&gt;</h4>
  <ul class="social">
    <li><span class="sq" style="background:#3b5b9a"></span>Friendwall</li>
    <li><span class="sq" style="background:#3a9ad8"></span>Chirper</li>
    <li><span class="sq" style="background:#2a78b0"></span>ProLink</li>
    <li><span class="sq" style="background:#c8261e"></span>ClipTube</li>
  </ul></div>
<div class="abs fcol" style="left:256px"><h4>A propos</h4>
  <ul><li>A propos de l'KRVT</li><li>Admissions</li><li>Calendrier de l'ecole</li><li>Offres d'emploi</li><li>Repertoire du personnel</li></ul></div>
<div class="abs fcol" style="left:401px"><h4>Etudiants</h4>
  <ul><li>Accueil - Etudiants</li><li>Programmes et Formations</li><li>Vie etudiante</li><li>Entreprises</li><li>Blogue</li></ul></div>
<div class="abs fcol" style="left:545px"><h4>KRVT</h4>
  <p>12, AVENUE DES ACACIAS<br>Ancienne route, Pres du Marché<br>Central</p>
  <ul style="margin-top:8px">
    <li style="display:flex;gap:6px;align-items:center"><svg width="12" height="12" viewBox="0 0 8 11"><path d="M2 0h2l1 3-1.5 1c.5 1.5 1 2.5 2 3.2L7 6l1 3-1 2C3 10 0 5 2 0z" fill="#fff"/></svg>(000) 41 552 18 30</li>
    <li style="display:flex;gap:6px;align-items:center"><svg width="12" height="12" viewBox="0 0 8 11"><path d="M2 0h2l1 3-1.5 1c.5 1.5 1 2.5 2 3.2L7 6l1 3-1 2C3 10 0 5 2 0z" fill="#fff"/></svg>(000) 47 903 26 14</li>
  </ul></div>
<div class="abs fcol" style="left:710px"><h4 style="width:60px">Infolettre</h4>
  <p style="width:115px;line-height:13.5px">Recevez les dernieres nouvelles de l'KRVT, ainsi Que des ressources utiles sur le management de projets.</p></div>
<div class="abs news-form"><span>ENVOYER</span></div>

<div class="abs copy">© 2014 Krvt. All right reserved.</div>

</body>
</html>
```